Founder / concept developer needs business card // Consultant needs VCARD

I need a business card for me as a founding consultant in Berlin. I advise entrepreneurs, especially in the design of business ideas, business plans or financing applications. More information about this in the annexes. My USP: I design / structure complex ideas and projects convincingly so that my client is successful. I want to communicate professionalism, effectiveness and clarity. Colors like from the range BLACK-GRAY-GREEN. I am 27 years old, I have studied business for 7 years. Attachments: - Business card design (only idea, do not focus on it) - Website screenshot (only idea, do not focus on it)

Target Market(s)

Target group: Founder (20-50 yrs, m / w, needy, in "break-up phase") and CONTRACTOR / "financier" (30-55 yrs, m / w, often public service "routine-oriented"). The foundations are in quite different industries: digital, craft, tourism, retail, services, etc. Almost all German.

Industry/Entity Type

Consultant

Contact Information for Business Card

Lukas Brandvik
M. Sc., International Business Administration
Gründungsberater, Konzeptentwickler
www.falkenhorn-beratung.de
kontakt@falkenhorn-beratung.de
Tel. 0471 239 5518

Colors

Designer to choose colors to be used in the design.

Requirements
Must have
• Professionalism, persuasiveness, clarity
Nice to have
• memorability
Should not have
• Schnörkelei

```html
<!DOCTYPE html>
<html lang="de">
<head>
<meta charset="utf-8">
<title>Falkenhorn Beratung – Visitenkarte</title>
<link rel="stylesheet" href="https://fonts.googleapis.com/css2?family=Source+Sans+3:wght@400;600&display=swap">
<style>
  :root {
    --backdrop: #646464;
    --card-light: #ffffff;
    --card-dark: #2c2d31;
    --green: #3a9f2c;
    --ink: #1f1f1f;
  }
  * { margin: 0; padding: 0; box-sizing: border-box; }
  html, body { width: 1200px; height: 900px; overflow: hidden; }
  body {
    background: var(--backdrop);
    font-family: "Source Sans 3", Arial, sans-serif;
    position: relative;
  }
  .card {
    position: absolute;
    top: 306px;
    width: 440px;
    height: 271px;
    border-radius: 12px;
  }
  .card--front { left: 149px; background: var(--card-light); }
  .card--back { left: 608px; background: var(--card-dark); }

  .brand {
    position: absolute;
    display: flex;
    align-items: center;
    gap: 7px;
    color: var(--green);
    font-weight: 600;
    text-transform: uppercase;
    white-space: nowrap;
  }
  .brand__square { display: block; background: var(--green); }
  .card--front .brand {
    left: 49px; top: 126px; font-size: 15px; letter-spacing: 0.5px;
  }
  .card--front .brand__square { width: 10px; height: 10px; }
  .card--back .brand {
    left: 50%; top: 50%; transform: translate(-50%, -50%);
    font-size: 26px; letter-spacing: 1px; gap: 10px;
  }
  .card--back .brand__square { width: 16px; height: 16px; }

  .divider {
    position: absolute;
    left: 210px; top: 72px;
    width: 1.5px; height: 127px;
    background: var(--green);
  }
  .contact {
    position: absolute;
    left: 239px; top: 69px;
    color: var(--ink);
  }
  .contact__name {
    color: var(--green);
    font-weight: 600;
    font-size: 15.5px;
    line-height: 18px;
    text-transform: uppercase;
    letter-spacing: 0.2px;
  }
  .contact__role { font-size: 12.5px; line-height: 15px; }
  .contact__list { list-style: none; margin-top: 12px; }
  .contact__item {
    display: flex; align-items: center; gap: 6px;
    font-size: 12.5px; line-height: 16px;
  }
  .contact__icon { width: 8px; height: 8px; fill: var(--green); flex: none; }
  .contact__address { margin-top: 7px; font-size: 12.5px; line-height: 16px; font-style: normal; }
</style>
</head>
<body>
  <section class="card card--front">
    <div class="brand"><span class="brand__square"></span>Falkenhorn</div>
    <div class="divider"></div>
    <div class="contact">
      <h1 class="contact__name">Lukas Brandvik</h1>
      <p class="contact__role">Managing Director</p>
      <ul class="contact__list">
        <li class="contact__item">
          <svg class="contact__icon" viewBox="0 0 10 10" aria-hidden="true"><path d="M2 0.5 L3.6 0.5 L4.2 2.8 L3 3.7 C3.6 5 4.8 6.3 6.2 7 L7.2 5.8 L9.5 6.4 L9.5 8 C9.5 9 8.8 9.5 8 9.5 C4 9.2 0.8 6 0.5 2 C0.5 1.2 1 0.5 2 0.5 Z"/></svg>
          0471 239 5518
        </li>
        <li class="contact__item">
          <svg class="contact__icon" viewBox="0 0 10 10" aria-hidden="true"><path d="M0.5 2 H9.5 V8.5 H0.5 Z M1.2 2.6 L5 5.4 L8.8 2.6 V3.4 L5 6.2 L1.2 3.4 Z" fill-rule="evenodd"/></svg>
          kontakt@falkenhorn-beratung.de
        </li>
        <li class="contact__item">
          <svg class="contact__icon" viewBox="0 0 10 10" aria-hidden="true"><circle cx="5" cy="5" r="4.5"/></svg>
          www.falkenhorn-beratung.de
        </li>
      </ul>
      <address class="contact__address">Torstraße 118, Berlin,<br>Deutschland, 10119</address>
    </div>
  </section>

  <section class="card card--back">
    <div class="brand"><span class="brand__square"></span>Falkenhorn</div>
  </section>
</body>
</html>
```